Bolt brace guard

We have created A revolutionary new design for door chains offering incredible strength and simplicity of instillation. Our product is called the Bolt Brace Guard. We are seeking a web site to promote and sell our lock. We want to promote that this lock is simple to install and much stronger than existing lock. www.boltbraceguards.com We are in the process of making a third video to replace the current one.. The first video is also on YouTube under toughest latch ever made early model test.

Target Market(s)

homeowners, apartments, dorm rooms, our someone wanting to turn a bedroom into a safe room ( somewhere they can go to in an emergency such as a break in).

Industry/Entity Type

Product

Font styles to use
Sans Serif

Requirements
Must have
• A video showing are product the weakness of existing door chains and the strength of are lock. A location where they can purchase our lock.
Nice to have
• A quick bio of the inventor of the lock a police officer for 22 years, retired but still concerned about safety and security

```html
<!DOCTYPE html>
<html lang="en">
<head>
<meta charset="utf-8">
<title>Bolt Brace Guards</title>
<link href="https://fonts.googleapis.com/css2?family=Roboto:wght@300;400;500;700&display=swap" rel="stylesheet">
<style>
:root{
  --blue:#2b86f6;
  --blue-dark:#1a6fd8;
  --black:#000;
  --white:#fff;
  --ink:#333;
  --body:#555;
  --panel:#e6e6e6;
  --hero-a:#8a6a45;
  --hero-b:#c8a27a;
}
*{margin:0;padding:0;box-sizing:border-box}
html,body{width:1200px;height:995px;overflow:hidden}
body{font-family:'Roboto',sans-serif;background:var(--panel);position:relative}
.site-header{position:absolute;left:0;top:0;width:1200px;height:139px;background:var(--blue)}
.brand{position:absolute;left:171px;top:36px;width:180px;text-align:center;color:var(--white)}
.brand-name{font-size:29px;font-weight:700;line-height:32px;text-transform:uppercase}
.phone{position:absolute;left:853px;top:33px;display:flex;align-items:center;color:var(--white);font-size:20px;font-weight:300;white-space:nowrap}
.phone-icon{width:36px;height:36px;border:1px solid #0b2f66;border-radius:50%;display:flex;align-items:center;justify-content:center;margin-right:10px}
.main-nav{position:absolute;top:88px;left:403px;height:51px;width:625px}
.nav-item{position:absolute;top:0;height:51px;line-height:54px;color:var(--white);font-size:14px;text-align:center;white-space:nowrap}
.nav-item.active{background:var(--black);border-radius:34px 34px 0 0;width:85px;left:0}
.nav-divider{position:absolute;top:16px;width:1px;height:26px;background:rgba(255,255,255,.5)}
.hero{position:absolute;left:0;top:139px;width:1200px;height:428px;background:radial-gradient(ellipse at 30% 40%,#6b4e33 0%,var(--hero-a) 40%,var(--hero-b) 100%)}
.hero-title{position:absolute;left:173px;top:124px;color:var(--white);font-size:35px;font-weight:400;line-height:35px;letter-spacing:.5px}
.hero-product{position:absolute;left:174px;top:204px;color:var(--white);font-size:42px;font-weight:700;white-space:nowrap}
.hero-btn{position:absolute;left:174px;top:267px;width:279px;height:40px;background:var(--blue);color:var(--white);font-size:14px;font-weight:500;display:flex;align-items:center;justify-content:center;gap:8px;border-radius:2px;white-space:nowrap}
.slider-dots{position:absolute;left:176px;top:327px;display:flex;gap:3px}
.dot{width:9px;height:9px;border-radius:50%;background:#ddd}
.dot.on{background:var(--blue)}
.video{position:absolute;left:613px;top:94px;width:391px;height:267px;border:3px solid var(--blue);background:#f2f2f2}
.video-frame{position:absolute;left:0;top:0;width:385px;height:230px;background:linear-gradient(90deg,#bdbdbd,#e4e4e2 45%,#cfcfcb)}
.play{position:absolute;left:165px;top:88px}
.video-bar{position:absolute;left:0;top:230px;width:385px;height:31px;background:#eee;border-top:1px solid #ccc}
.content{position:absolute;left:0;top:567px;width:1200px;height:294px}
.col{position:absolute;top:44px;width:265px}
.col h2{font-size:15.5px;font-weight:500;color:var(--ink);margin-bottom:14px;white-space:nowrap}
.col p{font-size:12px;font-weight:300;color:var(--body);line-height:17px}
.welcome p{width:268px}
.benefits{list-style:none}
.benefits li{font-size:12.5px;color:var(--ink);font-weight:300;line-height:16px;padding-left:17px;position:relative;margin-bottom:8px}
.benefits svg{position:absolute;left:0;top:3px}
.bio p{line-height:19px}
.bio-photo{float:right;width:94px;height:103px;background:linear-gradient(#4a5a78,#8a8a7a);margin:0 0 4px 10px}
.more{position:absolute;top:233px;height:32px;width:89px;background:var(--blue);color:var(--white);font-size:13px;font-weight:500;border-radius:2px;border:1px solid var(--blue-dark);display:flex;align-items:center;justify-content:center;gap:6px;white-space:nowrap}
.site-footer{position:absolute;left:0;top:861px;width:1200px;height:134px;background:var(--black);text-align:center}
.social{display:flex;justify-content:center;gap:22px;margin-top:37px}
.social span{width:12px;height:12px;border-radius:50%;background:var(--white)}
.legal{font-size:11.5px;color:var(--blue);margin-top:12px}
.address{font-size:11.5px;color:#ccc;margin-top:8px}
</style>
</head>
<body>
<header class="site-header">
  <div class="brand"><div class="brand-name">Bolt Brace Guards</div></div>
  <div class="phone"><span class="phone-icon"><svg width="16" height="16" viewBox="0 0 24 24"><path fill="#fff" d="M6.6 10.8a15 15 0 0 0 6.6 6.6l2.2-2.2a1 1 0 0 1 1-.25 11.4 11.4 0 0 0 3.6.57 1 1 0 0 1 1 1V20a1 1 0 0 1-1 1A17 17 0 0 1 3 4a1 1 0 0 1 1-1h3.5a1 1 0 0 1 1 1c0 1.25.2 2.45.57 3.57a1 1 0 0 1-.25 1z"/></svg></span>555-0142-7788</div>
  <nav class="main-nav">
    <span class="nav-item active">Home</span>
    <span class="nav-item" style="left:140px;width:70px">About Us</span>
    <span class="nav-divider" style="left:246px"></span>
    <span class="nav-item" style="left:287px;width:60px">Services</span>
    <span class="nav-divider" style="left:377px"></span>
    <span class="nav-item" style="left:429px;width:40px">Blogs</span>
    <span class="nav-divider" style="left:509px"></span>
    <span class="nav-item" style="left:550px;width:75px">Contact Us</span>
  </nav>
</header>
<section class="hero" role="img" aria-label="Blurred photo of a wooden door with a lock">
  <h1 class="hero-title">There is nothing else on<br>the market equal to</h1>
  <div class="hero-product">BOLT BRACE GUARDS</div>
  <a class="hero-btn">CLICK HERE TO VIEW MORE DETAIL <svg width="14" height="14" viewBox="0 0 14 14"><circle cx="7" cy="7" r="7" fill="#fff"/><path d="M4 7h5M7 4.5 9.5 7 7 9.5" stroke="#2b86f6" stroke-width="1.8" fill="none"/></svg></a>
  <div class="slider-dots"><span class="dot on"></span><span class="dot"></span><span class="dot"></span></div>
  <div class="video">
    <div class="video-frame" role="img" aria-label="Video still of a door chain lock on a white door"></div>
    <svg class="play" width="54" height="54" viewBox="0 0 54 54"><circle cx="27" cy="27" r="27" fill="#2b86f6"/><path d="M21 15 39 27 21 39z" fill="#fff"/></svg>
    <div class="video-bar"><svg width="385" height="31"><rect x="20" y="3" width="345" height="4" fill="#ccc"/><rect x="4" y="13" width="15" height="15" fill="#ddd" stroke="#999"/><path d="M9 16l6 4.5-6 4.5z" fill="#444"/><rect x="32" y="14" width="60" height="13" fill="#ddd"/><rect x="100" y="14" width="34" height="13" fill="#ddd"/><rect x="150" y="14" width="56" height="13" fill="#ddd"/><path d="M380 14v14h-50z" fill="#ddd" stroke="#999"/><path d="M338 28h14v-4z" fill="#3c3"/></svg></div>
  </div>
</section>
<main class="content">
  <div class="col welcome" style="left:173px">
    <h2>WELCOME TO BOLT BRACE GUARDS</h2>
    <p>Nunc eros justo, porttitor non nulla tempus, egestas blandit massa. Quisque sit amet dictum ante, tincidunt ultricies urna. Sed sed est ut dui commodo dignissim. Nunc dapibus erat id porttitor sodales. Aliquam nec neque a massa condimentum fermentum id eget ante. Fusce nec nulla nec tortor blandit scelerisque ut nec magna. Nulla vitae malesuada nunc, eu sagittis lorem.</p>
  </div>
  <a class="more" style="left:349px">View more <svg width="12" height="12" viewBox="0 0 14 14"><circle cx="7" cy="7" r="7" fill="#fff"/><path d="M4 7h5M7 4.5 9.5 7 7 9.5" stroke="#2b86f6" stroke-width="1.8" fill="none"/></svg></a>
  <div class="col" style="left:470px">
    <h2 style="font-size:16.5px">Bolt Brace Benefits</h2>
    <ul class="benefits">
      <li><svg width="12" height="11" viewBox="0 0 12 11"><rect x=".5" y="1.5" width="9" height="9" fill="none" stroke="#2b86f6"/><path d="M2.5 5.5 5 8 11 1" stroke="#2b86f6" stroke-width="2" fill="none"/></svg>Added safety and security , dual locks</li>
      <li><svg width="12" height="11" viewBox="0 0 12 11"><rect x=".5" y="1.5" width="9" height="9" fill="none" stroke="#2b86f6"/><path d="M2.5 5.5 5 8 11 1" stroke="#2b86f6" stroke-width="2" fill="none"/></svg>Stronger lock because of placement of lock</li>
      <li><svg width="12" height="11" viewBox="0 0 12 11"><rect x=".5" y="1.5" width="9" height="9" fill="none" stroke="#2b86f6"/><path d="M2.5 5.5 5 8 11 1" stroke="#2b86f6" stroke-width="2" fill="none"/></svg>screws are longer than screw on current door chains</li>
      <li><svg width="12" height="11" viewBox="0 0 12 11"><rect x=".5" y="1.5" width="9" height="9" fill="none" stroke="#2b86f6"/><path d="M2.5 5.5 5 8 11 1" stroke="#2b86f6" stroke-width="2" fill="none"/></svg>Better placement of screws</li>
      <li><svg width="12" height="11" viewBox="0 0 12 11"><rect x=".5" y="1.5" width="9" height="9" fill="none" stroke="#2b86f6"/><path d="M2.5 5.5 5 8 11 1" stroke="#2b86f6" stroke-width="2" fill="none"/></svg>Useable on all types of doors, wood, metal</li>
      <li><svg width="12" height="11" viewBox="0 0 12 11"><rect x=".5" y="1.5" width="9" height="9" fill="none" stroke="#2b86f6"/><path d="M2.5 5.5 5 8 11 1" stroke="#2b86f6" stroke-width="2" fill="none"/></svg>Ease of installation</li>
    </ul>
  </div>
  <a class="more" style="left:645px">View more <svg width="12" height="12" viewBox="0 0 14 14"><circle cx="7" cy="7" r="7" fill="#fff"/><path d="M4 7h5M7 4.5 9.5 7 7 9.5" stroke="#2b86f6" stroke-width="1.8" fill="none"/></svg></a>
  <div class="col bio" style="left:765px;width:263px">
    <h2>BIO OF THE INVENTOR</h2>
    <div class="bio-photo" role="img" aria-label="Portrait photo of the inventor in uniform"></div>
    <p>I retired from the Harbor County sheriff's department as a deputy sheriff after 22 years of service, because of a back injury. In February 2014. I suffered a major relapse with my back and was in the hospital for two weeks. I after the hospital I went home and</p>
  </div>
  <a class="more" style="left:940px">View more <svg width="12" height="12" viewBox="0 0 14 14"><circle cx="7" cy="7" r="7" fill="#fff"/><path d="M4 7h5M7 4.5 9.5 7 7 9.5" stroke="#2b86f6" stroke-width="1.8" fill="none"/></svg></a>
</main>
<footer class="site-footer">
  <div class="social"><span></span><span></span><span></span><span></span></div>
  <div class="legal">Copyright © 2014 - All rights reserved. Terms &amp; Condition &nbsp;|&nbsp; Privacy policy</div>
  <div class="address">418 Cedar Hollow Road Maple Falls, 555-0142-7788 &nbsp;|&nbsp; info@boltbraceguards.com</div>
</footer>
</body>
</html>
```